Rocket business card

Modern business card design, use of color is good with clean space too.

Things to include on card:

Quote: I add fuel to your optometry practice

- Eyewear Sales
- Admin Duties
- Revenue Collection
- Leadership
- Tech Adoption
- COGS Reduction
- Product Sourcing
-Medical Growth

Dalton Vessey, CEO
Glint Harbor
Text Me! 847-302-1964
dalton@glintharbor.example

```html
<!DOCTYPE html>
<html lang="en">
<head>
<meta charset="utf-8">
<title>Glint Harbor — Business Card</title>
<link href="https://fonts.googleapis.com/css2?family=Roboto:wght@400;500&display=swap" rel="stylesheet">
<style>
  :root {
    --bg: #2a2a2a;
    --card-front: #ffffff;
    --card-back: #1f1f21;
    --ink: #1a1a1a;
    --muted: #555555;
    --accent-red: #e8432a;
    --accent-orange: #f39a1e;
    --back-text: #e6e6e6;
    --rule: #444444;
  }
  * { margin: 0; padding: 0; box-sizing: border-box; }
  html, body { width: 1200px; height: 1108px; overflow: hidden; }
  body {
    background: var(--bg);
    font-family: "Roboto", Arial, sans-serif;
    display: flex;
    align-items: center;
    justify-content: center;
    gap: 80px;
  }
  .card {
    width: 480px;
    height: 840px;
    border-radius: 36px;
    position: relative;
    overflow: hidden;
  }
  /* Front */
  .card-front {
    background: var(--card-front);
    color: var(--ink);
    text-align: center;
  }
  .brand {
    position: absolute;
    top: 150px;
    left: 0; right: 0;
    display: flex;
    flex-direction: column;
    align-items: center;
    gap: 22px;
  }
  .brand-dot {
    width: 96px; height: 96px;
    border-radius: 50%;
    background: linear-gradient(135deg, var(--accent-red), var(--accent-orange));
  }
  .brand-name {
    font-size: 50px;
    font-weight: 400;
    letter-spacing: 2px;
    color: var(--ink);
    text-transform: uppercase;
  }
  .identity {
    position: absolute;
    top: 500px;
    left: 0; right: 0;
  }
  .person-name {
    font-size: 34px;
    font-weight: 500;
    text-transform: uppercase;
    background: linear-gradient(90deg, var(--accent-red), var(--accent-orange));
    -webkit-background-clip: text;
    background-clip: text;
    color: transparent;
    letter-spacing: 0.5px;
  }
  .person-role {
    font-size: 20px;
    color: var(--muted);
    margin-top: 4px;
  }
  .contact-divider {
    display: flex;
    align-items: center;
    justify-content: center;
    gap: 8px;
    margin: 14px auto 18px;
    width: 340px;
  }
  .contact-divider .rule { flex: 1; height: 1px; background: var(--muted); }
  .icon-badge {
    width: 30px; height: 30px;
    border-radius: 50%;
    background: linear-gradient(135deg, var(--accent-red), var(--accent-orange));
    display: flex; align-items: center; justify-content: center;
  }
  .contact-line { font-size: 22px; line-height: 34px; color: var(--ink); }

  /* Back */
  .card-back { background: var(--card-back); color: var(--back-text); }
  .back-texture {
    position: absolute;
    top: 0; left: 0; right: 0;
    height: 600px;
    background: linear-gradient(180deg, #2b2b2d 0%, #232325 70%, var(--card-back) 100%);
  }
  .back-mark {
    position: absolute;
    top: 612px;
    left: 50%;
    width: 38px; height: 38px;
    margin-left: -19px;
    border-radius: 50%;
    background: linear-gradient(135deg, var(--accent-red), var(--accent-orange));
  }
  .services {
    position: absolute;
    top: 672px;
    left: 0; right: 0;
    list-style: none;
    text-align: center;
    font-size: 21px;
    line-height: 33px;
  }
  .services .sep { margin: 0 8px; }
</style>
</head>
<body>
  <section class="card card-front">
    <div class="brand">
      <div class="brand-dot"></div>
      <div class="brand-name">Glint Harbor</div>
    </div>
    <div class="identity">
      <div class="person-name">Dalton Vessey</div>
      <div class="person-role">CEO</div>
      <div class="contact-divider">
        <span class="rule"></span>
        <span class="icon-badge">
          <svg width="16" height="16" viewBox="0 0 24 24" aria-hidden="true"><path fill="#fff" d="M6.6 10.8a15.1 15.1 0 0 0 6.6 6.6l2.2-2.2a1 1 0 0 1 1-.25 11.4 11.4 0 0 0 3.6.57 1 1 0 0 1 1 1V20a1 1 0 0 1-1 1A17 17 0 0 1 3 4a1 1 0 0 1 1-1h3.5a1 1 0 0 1 1 1c0 1.25.2 2.45.57 3.57a1 1 0 0 1-.25 1z"/></svg>
        </span>
        <span class="icon-badge">
          <svg width="16" height="16" viewBox="0 0 24 24" aria-hidden="true"><rect x="3" y="6" width="18" height="12" rx="1" fill="#fff"/><path d="M3 6l9 7 9-7" fill="none" stroke="#f0702a" stroke-width="1.8"/></svg>
        </span>
        <span class="rule"></span>
      </div>
      <div class="contact-line">847-302-1964</div>
      <div class="contact-line">dalton@glintharbor.example</div>
    </div>
  </section>

  <section class="card card-back">
    <div class="back-texture" role="img" aria-label="Faint repeating brand texture"></div>
    <div class="back-mark"></div>
    <ul class="services">
      <li>Eyewear Sales<span class="sep">•</span>Admin Duties</li>
      <li>Revenue Collection<span class="sep">•</span>Leadership</li>
      <li>Tech Adoption<span class="sep">•</span>COGS Reduction</li>
      <li>Product Sourcing<span class="sep">•</span>Medical Growth</li>
    </ul>
  </section>
</body>
</html>
```